Law Firm Website Update

I have an existing website but it is very wordy, not very aesthetically pleasing and I want additional features. I would like to update the areas of law and pictures, I would like to add a page for a client to fill in their information and links to other pages. Also want to make it more mobile friendly. site is www.brightmerelegal.com

Coding

Coded - Design and coding required

```html
<!DOCTYPE html>
<html lang="en">
<head>
<meta charset="utf-8">
<title>Brightmere Legal P.C. — Northern California Legal Guidance</title>
<link rel="stylesheet" href="https://fonts.googleapis.com/css2?family=Cinzel:wght@400;500;600&family=Poppins:wght@300;400;500;600&display=swap">
<style>
:root{
  --red:#e1262c;
  --red-dark:#c11a20;
  --ink:#1d1d1f;
  --text:#4a4a4a;
  --muted:#8a8a8a;
  --line:#e6e6e6;
  --paper:#ffffff;
  --dark:#1b1b1d;
  --wood:#6b4328;
  --serif:'Cinzel', serif;
  --sans:'Poppins', sans-serif;
}
*{box-sizing:border-box;margin:0;padding:0}
html,body{width:1200px;height:4916px;overflow:hidden}
body{position:relative;background:var(--paper);font-family:var(--sans);color:var(--text)}
.abs{position:absolute}
a{color:inherit;text-decoration:none}

/* header */
.site-header{top:0;left:0;width:1200px;height:140px;display:flex;align-items:center;padding:0 70px;background:#fff}
.brand{font-family:var(--serif);color:var(--red);font-size:34px;font-weight:500;line-height:1}
.brand small{display:block;font-size:15px;letter-spacing:3px;margin-top:4px;text-align:center}
.main-nav{display:flex;gap:34px;margin-left:auto;font-size:15px;color:var(--ink)}
.main-nav .active{font-weight:600;border-bottom:2px solid var(--red);padding-bottom:3px}
.btn{display:inline-block;background:var(--red);color:#fff;font-size:14px;font-weight:500;letter-spacing:.5px;padding:12px 24px;border-radius:30px}
.site-header .btn{margin-left:40px}

/* hero */
.hero{top:140px;left:0;width:1200px;height:760px;background:linear-gradient(120deg,#d9d4cd 0%,#a89a8a 30%,#6b4b33 60%,#3a2617 100%)}
.hero-circle{left:330px;top:80px;width:540px;height:540px;border-radius:50%;background:rgba(30,22,16,.58);display:flex;flex-direction:column;align-items:center;justify-content:center;text-align:center;color:#fff}
.hero-circle .kicker{font-family:var(--serif);font-size:34px}
.hero-circle h1{font-family:var(--serif);font-weight:400;font-size:64px;line-height:1.05}
.hero-circle .sub{font-family:var(--serif);font-size:26px;margin-bottom:14px}
.hero-circle p{font-size:19px;line-height:1.4;width:440px;margin-bottom:26px}
.dots{display:flex;gap:10px;justify-content:center}
.dots i{width:9px;height:9px;border-radius:50%;background:#ccc;display:block}
.dots i.on{background:var(--red)}
.hero .dots{position:absolute;bottom:28px;left:0;right:0}
.hero .dots i{background:#fff;opacity:.6}
.hero .dots i.on{opacity:1;background:#fff}

/* section heads */
.eyebrow{display:flex;align-items:center;gap:12px;color:var(--red);font-size:15px;letter-spacing:1px;font-weight:500}
.eyebrow::before,.eyebrow::after{content:"";height:1px;width:60px;background:var(--red)}
.eyebrow.left::before{width:0}
h2{font-family:var(--serif);font-weight:400;color:var(--ink);font-size:58px;line-height:1.1}
.center{text-align:center}
.center .eyebrow{justify-content:center}

/* about */
.about{top:960px;left:70px;width:600px}
.about h2{margin:8px 0 40px}
.about p{font-size:14.5px;line-height:1.85;margin-bottom:22px}
.about-photo-main{left:780px;top:1000px;width:350px;height:420px;background:linear-gradient(160deg,#2d2a28,#5a5148 60%,#8e8070)}
.about-photo-sub{left:690px;top:1240px;width:230px;height:300px;background:linear-gradient(150deg,#c59a5b,#7c5630 60%,#3b2616);border:8px solid #fff}

/* practice */
.practice-head{top:1670px;left:0;width:1200px}
.practice-map{top:1830px;left:0;width:1200px;height:470px}
.area{position:absolute;font-size:15px;color:var(--ink);line-height:1.3;width:200px}
.area.l{text-align:right}
.practice-logo{position:absolute;left:0;right:0;top:272px;text-align:center;font-family:var(--serif);color:#fff;font-size:40px;line-height:1}
.practice-logo small{display:block;font-size:18px;letter-spacing:4px;margin-top:4px}
.practice-cta{top:2290px;left:0;width:1200px;text-align:center}

/* attorney */
.att-photo{left:88px;top:2520px;width:350px;height:520px;background:linear-gradient(180deg,#e8e8e8,#bdbdbd)}
.att-badge{left:380px;top:2760px;width:180px;height:300px;background:var(--red);color:#fff;text-align:center;padding:28px 18px;border:6px solid #fff;box-shadow:0 6px 20px rgba(0,0,0,.15)}
.att-badge b{display:block;font-size:32px;font-weight:600;margin-top:12px}
.att-badge span{font-size:14px;line-height:1.4;display:block}
.att-text{left:620px;top:2560px;width:510px}
.att-text h2{font-size:52px;margin:6px 0 26px}
.att-text p{font-size:14.5px;line-height:1.85}

/* reviews */
.reviews-head{top:3140px;left:0;width:1200px}
.reviews-head p{font-size:14px;margin-top:18px}
.review{top:3390px;width:320px;height:300px;background:#fff;box-shadow:0 8px 28px rgba(0,0,0,.1);text-align:center;padding:34px 30px}
.review .qm{position:absolute;top:10px;right:20px;font-family:var(--serif);font-size:80px;color:#eee;line-height:1}
.review .stars{color:var(--red);font-size:14px;letter-spacing:2px}
.review h4{color:var(--red);font-weight:500;font-size:15px;margin:6px 0 14px}
.review p{font-size:14px;line-height:1.75}
.arrow{top:3520px;width:44px;height:44px;border-radius:50%;border:1px solid var(--line);display:flex;align-items:center;justify-content:center;background:#fff}
.reviews-dots{top:3710px;left:0;width:1200px}

/* contact */
.contact{top:3940px;left:0;width:1200px;height:600px;background:linear-gradient(90deg,var(--dark) 0%,var(--dark) 45%,#3b332c 70%,#8a7660 100%)}
.contact-inner{position:absolute;left:70px;top:60px;width:560px;color:#fff}
.contact-inner .eyebrow{color:var(--red)}
.contact-inner h2{color:#fff;margin:6px 0 14px}
.contact-inner .lead{font-size:14px;margin-bottom:26px}
.field-row{display:flex;gap:14px;margin-bottom:14px}
.field{flex:1;height:44px;background:#fff;color:var(--muted);font-size:13px;padding:13px 14px}
.field.msg{height:120px}
.contact-inner .btn{margin-top:10px}

/* footer */
.site-footer{top:4540px;left:0;width:1200px;height:320px;background:var(--red);color:#fff}
.site-footer h3{font-family:var(--serif);font-weight:400;font-size:22px;margin-bottom:18px}
.f-links{position:absolute;left:90px;top:70px;display:flex;gap:60px;font-size:14px}
.f-links ul{list-style:none;line-height:2}
.f-links li::before{content:"› ";}
.f-brand{position:absolute;left:400px;width:400px;top:80px;text-align:center}
.f-brand .brand{color:#fff;font-size:44px}
.f-brand .brand small{font-size:18px}
.f-brand .btn{background:transparent;border:1px solid #fff;margin-top:34px}
.f-contact{position:absolute;left:900px;top:70px;font-size:14px;width:230px}
.f-item{display:flex;gap:12px;margin-bottom:14px;line-height:1.4}
.f-item svg{flex:none;margin-top:3px}
.copyright{top:4860px;left:0;width:1200px;height:56px;display:flex;align-items:center;justify-content:center;font-size:13px;color:var(--ink);background:#fff}
</style>
</head>
<body>

<header class="site-header abs">
  <div class="brand">Brightmere Legal<small>P.C.</small></div>
  <nav class="main-nav">
    <a class="active">Home</a><a>About Us</a><a>Attorney Profile</a><a>Practice Areas ▾</a><a>Reviews</a><a>Pay Online</a><a>Contact Us</a>
  </nav>
  <a class="btn">FREE CONSULTATION</a>
</header>

<section class="hero abs" role="img" aria-label="Courtroom desk with a wooden judge's gavel and scales">
  <div class="hero-circle abs">
    <div class="kicker">Northern California</div>
    <h1>LEGAL GUIDANCE</h1>
    <div class="sub">FOR INDIVIDUALS &amp; BUSINESSES</div>
    <p>Providing clients with sound legal advice, fluid communication &amp; prompt service</p>
    <a class="btn">CONTACT US ›</a>
  </div>
  <div class="dots"><i class="on"></i><i></i><i></i></div>
</section>

<section class="about abs">
  <div class="eyebrow left">WHO WE ARE</div>
  <h2>About Us</h2>
  <p>Brightmere Legal P.C. offers a boutique law firm option for clients who want to enjoy all the advantages of big-firm style representation in a personal and professional environment. Our off-the-box legal strategies that have made the seemingly impossible, possible. Our approach begins with a no-cost consultation to assess our client's needs and evaluate their position in the matter at hand. We strive to meet and exceed our firm mission to provide each and every client with sound legal advice, fluid communication and prompt service.</p>
  <p>Brightmere Legal P.C. is led by Elena R. Marsh, a dedicated and caring professional who uses her broad range of skills as a California lawyer to bring consumers and business owners exceptionally strong legal representation aimed at achieving the best results for her clients. She works with people from all over Northern California in the areas of Real Estate law, Business Law, Bankruptcy, Franchise Law and Civil Litigation.</p>
</section>
<div class="about-photo-main abs" role="img" aria-label="Lawyer reviewing documents at a desk"></div>
<div class="about-photo-sub abs" role="img" aria-label="Brass scales of justice beside law books"></div>

<section class="practice-head abs center">
  <div class="eyebrow">WHAT WE DO</div>
  <h2>PRACTICE AREAS</h2>
</section>

<div class="practice-map abs">
  <svg class="abs" style="left:0;top:0" width="1200" height="470" viewBox="0 0 1200 470">
    <defs>
      <linearGradient id="gavelTone" x1="0" y1="0" x2="1" y2="1">
        <stop offset="0" stop-color="#c9b8a6"/><stop offset=".5" stop-color="#7a5236"/><stop offset="1" stop-color="#3a2415"/>
      </linearGradient>
    </defs>
    <path d="M300 420 A300 330 0 0 1 900 420" fill="none" stroke="#e9c2c3" stroke-width="2"/>
    <path d="M250 430 A350 380 0 0 1 950 430" fill="none" stroke="#f1dede" stroke-width="1"/>
    <path d="M420 440 L420 330 A180 170 0 0 1 780 330 L780 440 Z" fill="url(#gavelTone)" role="img" aria-label="Gavel resting on a sound block"/>
    <g fill="#e1262c">
      <circle cx="470" cy="70" r="20"/><circle cx="730" cy="70" r="20"/>
      <circle cx="370" cy="140" r="20"/><circle cx="830" cy="140" r="20"/>
      <circle cx="310" cy="230" r="20"/><circle cx="890" cy="230" r="20"/>
      <circle cx="290" cy="340" r="20"/><circle cx="910" cy="340" r="20"/>
    </g>
    <g fill="none" stroke="#fff" stroke-width="2">
      <circle cx="470" cy="70" r="8"/><circle cx="730" cy="70" r="8"/>
      <circle cx="370" cy="140" r="8"/><circle cx="830" cy="140" r="8"/>
      <circle cx="310" cy="230" r="8"/><circle cx="890" cy="230" r="8"/>
      <circle cx="290" cy="340" r="8"/><circle cx="910" cy="340" r="8"/>
    </g>
  </svg>
  <div class="area l" style="left:230px;top:60px">Franchise Law</div>
  <div class="area" style="left:762px;top:60px">Civil Litigation</div>
  <div class="area l" style="left:130px;top:130px">Business Law</div>
  <div class="area" style="left:862px;top:120px">Alternative Dispute<br>Resolution</div>
  <div class="area l" style="left:70px;top:210px">Commercial Real Estate<br>Transactions</div>
  <div class="area" style="left:922px;top:220px">Estate Planning</div>
  <div class="area l" style="left:50px;top:330px">Real Estate</div>
  <div class="area" style="left:942px;top:330px">Bankruptcy</div>
  <div class="practice-logo">Brightmere Legal<small>P.C.</small></div>
</div>
<div class="practice-cta abs"><a class="btn">CONTACT US ›</a></div>

<div class="att-photo abs" role="img" aria-label="Portrait of the firm's attorney"></div>
<div class="att-badge abs">
  <svg width="40" height="40" viewBox="0 0 40 40"><circle cx="20" cy="16" r="11" fill="none" stroke="#fff" stroke-width="2"/><path d="M13 25 L10 37 L20 32 L30 37 L27 25" fill="none" stroke="#fff" stroke-width="2"/></svg>
  <b>20 years</b>
  <span>of business management, operations and marketing experience</span>
</div>
<section class="att-text abs">
  <div class="eyebrow left">ATTORNEY</div>
  <h2>ELENA R. MARSH</h2>
  <p>Elena Marsh is a California real estate attorney and principal of Brightmere Legal P.C. specializing in corporate law, business law, contract law and real estate law. She is also principal and managing broker of her real estate firm, a property management and real estate investment company. She holds a degree in Business Administration, Marketing and a Juris Doctorate from a Northern California university. She formerly served as the Executive Marketing Director and Director of Development for a national trade association.</p>
</section>

<section class="reviews-head abs center">
  <div class="eyebrow">TESTIMONIALS</div>
  <h2>REVIEWS AND RATINGS</h2>
  <p>Our reviews are compiled from our profiles on trusted legal directories.</p>
</section>
<div class="arrow abs" style="left:160px"><svg width="14" height="14" viewBox="0 0 14 14"><path d="M9 2 L4 7 L9 12" fill="none" stroke="#555" stroke-width="2"/></svg></div>
<article class="review abs" style="left:255px">
  <span class="qm">“</span>
  <div class="stars">★★★★★</div>
  <h4>Client</h4>
  <p>A very smart attorney. I said always on my corner. She is down to earth and very real with you. She can think outside the box which is why she is so good. She was a great help to my uncle and I would highly recommend her!</p>
</article>
<article class="review abs" style="left:625px">
  <span class="qm">“</span>
  <div class="stars">★★★★★</div>
  <h4>Client</h4>
  <p>I really enjoyed working with Elena. She assisted us in our corporation set up as well as some real estate transactions. She is professional and excellent at what she does.</p>
</article>
<div class="arrow abs" style="left:996px"><svg width="14" height="14" viewBox="0 0 14 14"><path d="M5 2 L10 7 L5 12" fill="none" stroke="#555" stroke-width="2"/></svg></div>
<div class="reviews-dots abs"><div class="dots"><i class="on"></i><i></i><i></i></div></div>

<section class="contact abs" aria-label="Contact form">
  <div class="abs" style="right:0;top:0;width:560px;height:600px" role="img" aria-label="Lawyer at a desk with scales of justice and a gavel"></div>
  <div class="contact-inner">
    <div class="eyebrow left">BRIGHTMERE LEGAL</div>
    <h2>Contact Us</h2>
    <p class="lead">Please fill out the form below and one of our attorneys will contact you.</p>
    <div class="field-row"><div class="field">Full Name</div><div class="field">Phone Number</div></div>
    <div class="field-row"><div class="field">Email Address</div></div>
    <div class="field-row"><div class="field msg">Message</div></div>
    <a class="btn">SUBMIT NOW ›</a>
  </div>
</section>

<footer class="site-footer abs">
  <div class="f-links">
    <div>
      <h3>QUICK LINKS</h3>
      <ul><li>Home</li><li>About Us</li><li>Practice Areas</li><li>Reviews</li><li>Pay Online</li></ul>
    </div>
    <div>
      <h3>&nbsp;</h3>
      <ul><li>Blog</li><li>Contact Us</li><li>Map &amp; Directions</li></ul>
    </div>
  </div>
  <div class="f-brand">
    <div class="brand">Brightmere Legal<small>P.C.</small></div>
    <a class="btn">FREE CONSULTATION</a>
  </div>
  <div class="f-contact">
    <h3>CONTACT US</h3>
    <div class="f-item"><svg width="18" height="18" viewBox="0 0 18 18"><path d="M4 2 L7 2 L8 6 L6 7.5 C7 10 8 11 10.5 12 L12 10 L16 11 L16 14 C16 15 15 16 14 16 C8 16 2 10 2 4 C2 3 3 2 4 2Z" fill="#fff"/></svg><div>Call Us<br>555-0148</div></div>
    <div class="f-item"><svg width="18" height="18" viewBox="0 0 18 18"><rect x="2" y="6" width="14" height="8" fill="none" stroke="#fff" stroke-width="1.6"/><rect x="5" y="2" width="8" height="4" fill="none" stroke="#fff" stroke-width="1.6"/></svg><div>Fax Us<br>555-0192</div></div>
    <div class="f-item"><svg width="18" height="18" viewBox="0 0 18 18"><path d="M9 1 C5 1 3 4 3 7 C3 11 9 17 9 17 C9 17 15 11 15 7 C15 4 13 1 9 1Z" fill="#fff"/><circle cx="9" cy="7" r="2.3" fill="#e1262c"/></svg><div>418 Alder Grove Avenue,<br>Suite C, Larkspur Valley,<br>California 95000</div></div>
  </div>
</footer>
<div class="copyright abs">Copyright © 2025 All Rights Reserved By Brightmere Legal P.C.</div>

</body>
</html>
```